I have looking for nice Photo for my Business Cards , see below details I justed send.

Please see my Website Link , It should be up and running my late tonight or tomorrow morning.

http://www.coralbreezeescapes.net

Travel & Toursim

Company Name: Coral Breeze Escapes

If you look at my Website it will show you photos that keep changing at the top. I want something like that or if you have some samples to show me.
Looking for a beach with sand and maybe having somebody resting on the beach with a drink or reading.

Let me know what you think.

Also what will be the cost hopefully you already got some photos to show me. I want my business Card to be glossy.

Business

Contact: Delphine Orvak
Mobile: 0437 912 654
Email: delphine@coralbreezetrips.com
Website: www.coralbreezeescapes.net

• Company Name: Coral Breeze Escapes
Contact: Delphine Orvak
Mobile: 0437 912 654

```html
<!DOCTYPE html>
<html lang="en">
<head>
<meta charset="utf-8">
<title>Coral Breeze Escapes – Business Card</title>
<link href="https://fonts.googleapis.com/css2?family=Bebas+Neue&family=Open+Sans:wght@400&display=swap" rel="stylesheet">
<style>
  :root {
    --page-bg: #e9e7ea;
    --card-black: #000000;
    --text-white: #ffffff;
    --text-soft: #d8d8d8;
    --text-muted: #8a8a8a;
    --sky-top: #6f9fdc;
    --sky-mid: #9cc0ea;
    --sea: #4f6f8c;
    --shore: #2d3440;
  }
  * { box-sizing: border-box; margin: 0; padding: 0; }
  html, body {
    width: 1200px;
    height: 800px;
    overflow: hidden;
    background: var(--page-bg);
  }
  .sheet {
    position: relative;
    width: 1200px;
    height: 800px;
    display: flex;
    align-items: center;
    justify-content: center;
    gap: 40px;
  }
  .card {
    position: relative;
    width: 520px;
    height: 298px;
    overflow: hidden;
    box-shadow: 0 6px 18px rgba(0,0,0,0.18);
  }

  /* Front side */
  .card-front__photo {
    position: absolute;
    inset: 0;
    background:
      linear-gradient(180deg, var(--sky-top) 0%, var(--sky-mid) 55%, var(--sea) 78%, var(--shore) 100%);
  }
  .card-front__title {
    position: absolute;
    right: 22px;
    bottom: 22px;
    font-family: "Bebas Neue", "Arial Narrow", sans-serif;
    font-size: 40px;
    letter-spacing: 1px;
    color: var(--text-white);
    line-height: 1;
  }

  /* Back side */
  .card-back {
    background: var(--card-black);
    color: var(--text-white);
  }
  .card-back__title {
    position: absolute;
    top: 28px;
    right: 26px;
    font-family: "Bebas Neue", "Arial Narrow", sans-serif;
    font-size: 44px;
    letter-spacing: 4px;
    line-height: 1;
    color: var(--text-white);
    text-shadow: 0 0 6px rgba(255,255,255,0.35);
  }
  .card-back__name {
    position: absolute;
    top: 118px;
    left: 0;
    right: 0;
    text-align: center;
    font-family: "Open Sans", Arial, sans-serif;
    font-size: 20px;
    letter-spacing: 0.5px;
    color: var(--text-white);
  }
  .card-back__contact {
    position: absolute;
    top: 168px;
    left: 0;
    right: 0;
    text-align: center;
    font-family: "Open Sans", Arial, sans-serif;
    font-size: 15px;
    line-height: 1.45;
  }
  .card-back__label { color: var(--text-white); font-size: 14px; }
  .card-back__phone { color: var(--text-soft); }
  .card-back__email,
  .card-back__web { color: var(--text-muted); }
</style>
</head>
<body>
  <main class="sheet">
    <section class="card card-front">
      <div class="card-front__photo" role="img" aria-label="Photo of a couple relaxing in white beach chairs by the sea under a clear blue sky"></div>
      <h1 class="card-front__title">Coral Breeze Escapes</h1>
    </section>

    <section class="card card-back">
      <h2 class="card-back__title">CORAL BREEZE ESCAPES</h2>
      <p class="card-back__name">DELPHINE ORVAK</p>
      <div class="card-back__contact">
        <p class="card-back__label">CONTACT:</p>
        <p class="card-back__phone">0437 912 654</p>
        <p class="card-back__email">delphine@coralbreezetrips.com</p>
        <p class="card-back__web">www.coralbreezeescapes.net</p>
      </div>
    </section>
  </main>
</body>
</html>
```